Design Spot Gloss Business Card with Rounded Corners

Colors: Red, White, Black (maybe gray)

Side 1:

centered logo with simple / minimal / clean background (SEE ATTACHED LOGO FILE)

Side 2:

Dale Mirwick
Founder/President

(o) 617-503-2291
Email: dale@[login to view URL]

DESIGN NOTES & REQUIREMENTS:

+ Please find a way to DRAW ATTENTION to the ".co" extension (perhaps by using a different color) so that people pay attention to the .co and do not enter .com

+ Please include 1/4" round corners in design mock (if you can)

+ Card will be printed using SPOT UV / GLOSS so use your best design judgement as to which design elements to highlight using this production method

```html
<!DOCTYPE html>
<html lang="en">
<head>
<meta charset="utf-8">
<title>Harlow Reach Management Group – Business Card</title>
<link href="https://fonts.googleapis.com/css2?family=Arimo:wght@400;700&family=Montserrat:wght@300;400&display=swap" rel="stylesheet">
<style>
  :root {
    --stage-light: #d6d6d6;
    --stage-dark: #8f8f8f;
    --card-core: #3a3a3a;
    --card-edge: #141414;
    --ink-white: #ffffff;
    --ink-gray: #bdbdbd;
    --ink-red: #e0251f;
  }
  * { margin: 0; padding: 0; box-sizing: border-box; }
  html, body {
    width: 1200px;
    height: 952px;
    overflow: hidden;
  }
  body {
    position: relative;
    background: linear-gradient(200deg, var(--stage-light) 0%, #b4b4b4 45%, var(--stage-dark) 100%);
    font-family: "Arimo", Arial, sans-serif;
  }
  .card {
    position: absolute;
    width: 628px;
    height: 380px;
    border-radius: 28px;
    overflow: hidden;
    background:
      radial-gradient(ellipse 55% 60% at 50% 45%, rgba(255,255,255,0.12), rgba(255,255,255,0) 70%),
      linear-gradient(90deg, var(--card-edge) 0%, var(--card-core) 50%, var(--card-edge) 100%);
    box-shadow: 0 8px 18px rgba(0,0,0,0.35);
  }
  .card--front { left: 56px; top: 92px; }
  .card--back { left: 512px; top: 505px; }

  .brand {
    position: absolute;
    left: 0; right: 0;
    top: 118px;
    text-align: center;
  }
  .brand__name {
    display: inline-flex;
    align-items: center;
    gap: 14px;
    font-family: "Arimo", Arial, sans-serif;
    font-weight: 700;
    font-size: 44px;
    letter-spacing: 2px;
    color: var(--ink-white);
    text-transform: uppercase;
  }
  .brand__dot {
    width: 22px; height: 22px;
    border-radius: 50%;
    background: var(--ink-red);
  }
  .brand__group {
    margin-top: 28px;
    font-family: "Montserrat", Arial, sans-serif;
    font-weight: 300;
    font-size: 26px;
    letter-spacing: 3px;
    color: var(--ink-gray);
    text-transform: uppercase;
  }
  .brand__services {
    margin-top: 8px;
    font-family: "Montserrat", Arial, sans-serif;
    font-size: 8px;
    letter-spacing: 1.5px;
    color: var(--ink-gray);
    text-transform: uppercase;
  }

  .person {
    position: absolute;
    left: 44px;
    top: 64px;
    font-size: 22px;
    line-height: 27px;
  }
  .person__name { color: var(--ink-red); padding-left: 20px; }
  .person__title { color: var(--ink-white); }

  .contact {
    position: absolute;
    right: 48px;
    top: 232px;
    text-align: right;
    color: var(--ink-white);
    font-size: 22px;
    line-height: 26px;
  }
  .contact__label { display: block; padding-right: 62px; }
  .contact__ext { color: var(--ink-red); }
</style>
</head>
<body>
  <section class="card card--front" aria-label="Card front">
    <div class="brand">
      <div class="brand__name"><span class="brand__dot"></span>Harlow Reach</div>
      <div class="brand__group">Management Group</div>
      <div class="brand__services">Branding • Marketing • Representation</div>
    </div>
  </section>

  <section class="card card--back" aria-label="Card back">
    <div class="person">
      <div class="person__name">Dale Mirwick</div>
      <div class="person__title">Founder/President</div>
    </div>
    <div class="contact">
      <div class="contact__phone">(o) 617-503-2291</div>
      <span class="contact__label">Email:</span>
      <div class="contact__email">dale@HRmgmt<span class="contact__ext">.co</span></div>
      <div class="contact__web">www.HRmgmt<span class="contact__ext">.co</span></div>
    </div>
  </section>
</body>
</html>
```